Business Card Design Project

Attached is a rough business card design. We like this general design but we feel that the layout, text, color can use improvement and we seek the help of a professional designer.
We have a television and film production company based in New York. We need our cards for television network executives, other production executives, financiers etc. We deal with creative types as well as business people so we need the card to be interesting and edgy just like the name of our company - KICKTHEDOOR. The design should reflect the edgy, punk rock attitude of our company.
We prefer orange typeface for the logo but we're open to other ideas. I am attaching our existing business card and other files to help with the design.
Thank you in advance!!
Updates
Target Market(s)
Television and film producers, television network executives, other production executives, financiers, distribution companies
Industry/Entity Type
Film Production
Requirements
Must have
- I am attaching a photo of the company mascot which is a dog. We prefer to have the dog's photo as part of the card but we're open to the other ideas.
Name, phone number, email

```html
<!DOCTYPE html>
<html lang="en">
<head>
<meta charset="utf-8">
<title>Kickthedoor Business Card</title>
<link rel="stylesheet" href="https://fonts.googleapis.com/css2?family=Ubuntu:wght@700&family=Questrial&display=swap">
<style>
  :root {
    --stage: #2b2f31;
    --card-top: #1f2224;
    --card-bottom: #121415;
    --brand-red: #d9231d;
    --label-red: #c8201a;
    --text-light: #e6e8e8;
    --text-soft: #c9cccc;
    --glow-teal: rgba(95, 179, 176, 0.32);
    --glow-green: rgba(63, 138, 85, 0.22);
    --photo-warm: #b07a58;
    --photo-floor: #e4c9c4;
  }
  * { margin: 0; padding: 0; box-sizing: border-box; }
  html, body { width: 1200px; height: 741px; overflow: hidden; }
  body {
    background: var(--stage);
    position: relative;
    font-family: "Questrial", sans-serif;
  }
  .card {
    position: absolute;
    width: 560px;
    height: 320px;
    top: 210px;
    background: linear-gradient(160deg, var(--card-top), var(--card-bottom));
    overflow: hidden;
    box-shadow: 0 12px 30px rgba(0,0,0,0.45);
  }
  .card--back { left: 25px; }
  .card--front { left: 615px; }
  .streak-area {
    position: absolute;
    pointer-events: none;
  }
  .card--back .streak-area {
    left: 0; right: 0; bottom: 0;
    height: 150px;
    background: radial-gradient(ellipse 90% 70% at 20% 100%, var(--glow-teal), var(--glow-green) 45%, transparent 75%);
  }
  .card--front .streak-area {
    right: 0; bottom: 0;
    width: 360px;
    height: 260px;
    background: radial-gradient(ellipse 80% 80% at 85% 85%, var(--glow-teal), var(--glow-green) 45%, transparent 75%);
  }
  .brand-name {
    position: absolute;
    font-family: "Ubuntu", sans-serif;
    font-weight: 700;
    color: var(--brand-red);
    letter-spacing: 1px;
    white-space: nowrap;
  }
  .card--back .brand-name {
    font-size: 44px;
    left: 0; right: 0;
    top: 112px;
    text-align: center;
  }
  .card--front .brand-name {
    font-size: 40px;
    left: 34px;
    top: 96px;
  }
  .person-name {
    position: absolute;
    left: 50px;
    top: 166px;
    font-size: 27px;
    color: var(--text-light);
    letter-spacing: 1px;
    white-space: nowrap;
  }
  .contact-list {
    position: absolute;
    left: 52px;
    top: 214px;
    list-style: none;
    font-size: 13px;
    line-height: 24px;
    white-space: nowrap;
  }
  .contact-label {
    display: inline-block;
    width: 60px;
    color: var(--label-red);
  }
  .contact-value { color: var(--text-soft); letter-spacing: 0.5px; }
  .mascot-photo {
    position: absolute;
    right: 28px;
    top: 22px;
    width: 210px;
    height: 150px;
  }
</style>
</head>
<body>

  <section class="card card--back" aria-label="Card back">
    <div class="streak-area" role="img" aria-label="Soft teal and green light streaks along the lower edge"></div>
    <div class="brand-name">Kickthedoor</div>
  </section>

  <section class="card card--front" aria-label="Card front">
    <div class="streak-area" role="img" aria-label="Soft teal and green light streaks across the lower right"></div>

    <svg class="mascot-photo" viewBox="0 0 210 150" role="img" aria-label="Photo of the company dog mascot">
      <defs>
        <linearGradient id="mascot-fill" x1="0" y1="0" x2="0" y2="1">
          <stop offset="0" stop-color="var(--photo-floor)"/>
          <stop offset="0.55" stop-color="var(--photo-warm)"/>
          <stop offset="1" stop-color="var(--photo-floor)"/>
        </linearGradient>
      </defs>
      <rect x="30" y="8" width="170" height="120" fill="#ffffff" opacity="0.25" transform="rotate(6 115 68)"/>
      <rect x="14" y="14" width="170" height="120" fill="#f2dcdc" opacity="0.45" transform="rotate(-5 99 74)"/>
      <rect x="22" y="18" width="166" height="116" fill="url(#mascot-fill)" stroke="#f4e6e6" stroke-width="4"/>
    </svg>

    <div class="brand-name">Kickthedoor</div>
    <div class="person-name">Daniel Moreland</div>
    <ul class="contact-list">
      <li><span class="contact-label">Phone :</span><span class="contact-value">917-555-0148</span></li>
      <li><span class="contact-label">Email</span><span class="contact-value">:daniel@kickthedoor.com</span></li>
    </ul>
  </section>

</body>
</html>
```